1 page infographic to highlight impact of an educational nonprofit

Our educational non-profit is celebrating our 10th Anniversary/Decade of Impact this year and would like to create a one page infographic to highlight our achievements.

Target Market(s)

Supporters of our educational non-profit

Industry/Entity Type

Education

Font styles to use
Serif

Colors
0556a4
f78f20
ffffff

Requirements
Must have
• Highlight statistics, create appropriate icons, include attached logos and pictures. Create pie charts and graphs to highlight results.
Should not have
• Please don't pick and choose statistics. Let me know if you can't fit it all in

```html
<!DOCTYPE html>
<html lang="en">
<head>
<meta charset="utf-8">
<title>A Decade of Impact</title>
<link rel="stylesheet" href="https://fonts.googleapis.com/css2?family=Oswald:wght@500;700&family=Open+Sans:wght@400;600;700&display=swap">
<style>
:root{
  --blue:#0556a4;
  --blue-dark:#043f7a;
  --orange:#f78f20;
  --white:#ffffff;
  --ink:#1f2f46;
  --grey:#8a94a3;
  --rule:#c9d6e6;
  --gold:#d6a72c;
}
*{box-sizing:border-box;margin:0;padding:0}
html,body{width:1200px;height:2308px;overflow:hidden;background:var(--white)}
body{font-family:"Open Sans",Arial,sans-serif;color:var(--ink)}
.canvas{position:relative;width:1200px;height:2308px;overflow:hidden;background:var(--white);border:6px solid var(--rule)}
.abs{position:absolute}
.display{font-family:"Oswald","Arial Narrow",sans-serif;font-weight:700;line-height:1}
.num-orange{color:var(--orange)}
.num-blue{color:var(--blue)}
.label{font-size:17px;line-height:1.3;color:var(--blue);font-weight:600}
.label-sm{font-size:15px;line-height:1.3;color:var(--ink)}

.brand{left:22px;top:26px;width:220px;display:flex;align-items:center;gap:10px}
.brand-dot{width:34px;height:34px;border-radius:50%;background:var(--orange)}
.brand-name{font-family:"Oswald",sans-serif;font-weight:700;font-size:44px;color:var(--blue)}
.brand-sub{left:22px;top:84px;font-size:13px;color:var(--blue);font-weight:600;letter-spacing:1px}
.banner{left:250px;top:22px;width:930px;height:92px;background:var(--blue);border-radius:12px;display:flex;align-items:center;justify-content:center}
.banner h1{font-family:"Oswald",sans-serif;font-weight:700;font-size:62px;color:var(--white);letter-spacing:2px}

.photo{left:22px;top:276px;width:390px;height:226px;border-radius:6px;background:linear-gradient(160deg,#cfe3f5 0%,#9bbfe0 55%,#5d8fbf 100%)}
.gender-head{left:800px;top:276px;width:360px;height:70px;background:var(--orange);color:var(--white);font-family:"Oswald",sans-serif;font-weight:700;font-size:40px;display:flex;align-items:center;justify-content:center;border-radius:6px}

.eth-box{left:22px;top:760px;width:440px;height:280px;border:3px solid var(--rule);border-radius:8px}
.eth-title{left:22px;top:760px;width:180px;height:44px;background:var(--orange);color:var(--white);font-family:"Oswald",sans-serif;font-weight:700;font-size:26px;display:flex;align-items:center;justify-content:center;border-radius:6px 0 6px 0}
.legend{font-size:15px;font-weight:600;color:var(--ink);display:flex;align-items:center;gap:8px}
.swatch{width:14px;height:14px;border-radius:50%;display:inline-block;flex:none}

.progress{left:420px;top:1070px;width:760px;height:830px;background:var(--blue);border-radius:10px}
.progress-year{left:450px;top:1092px;font-family:"Oswald",sans-serif;font-weight:700;font-size:74px;color:var(--white)}
.progress-tag{left:640px;top:1104px;font-family:"Oswald",sans-serif;font-weight:500;font-size:32px;line-height:1.15;color:var(--white)}
.income-figure{left:530px;top:1222px;font-family:"Oswald",sans-serif;font-weight:700;font-size:54px;color:var(--white)}
.income-label{left:530px;top:1288px;font-size:22px;color:var(--white);font-weight:600}
.income-legend{left:900px;top:1440px;display:flex;flex-direction:column;gap:34px}
.income-legend .legend{color:var(--white);font-size:20px}

.badge{left:40px;top:1080px;width:150px;height:150px;border-radius:50%;background:var(--gold)}
.rule{height:3px;background:var(--rule)}
.partners{left:770px;top:1940px;width:410px;display:grid;grid-template-columns:1fr 1fr;gap:22px 20px}
.partner{display:flex;align-items:center;gap:10px;font-weight:700;font-size:19px;color:var(--blue);height:60px}
.partner-mark{width:22px;height:22px;background:var(--blue);flex:none}
</style>
</head>
<body>
<div class="canvas">

  <!-- Header -->
  <div class="abs brand"><span class="brand-dot"></span><span class="brand-name">Pathway</span></div>
  <div class="abs brand-sub">YOUTH ACADEMY</div>
  <div class="abs banner"><h1>A DECADE OF IMPACT</h1></div>

  <!-- Row 1: headline stats -->
  <svg class="abs" style="left:22px;top:150px" width="80" height="70" viewBox="0 0 80 70" aria-hidden="true">
    <polygon points="40,6 78,24 40,42 2,24" fill="var(--orange)"/>
    <path d="M18 32 V50 Q40 64 62 50 V32 L40 44 Z" fill="var(--orange)"/>
    <rect x="70" y="24" width="4" height="26" fill="var(--orange)"/>
  </svg>
  <div class="abs display num-orange" style="left:110px;top:150px;font-size:58px">100%</div>
  <div class="abs label-sm" style="left:112px;top:216px;width:200px">High school Graduation Rate</div>

  <div class="abs display num-orange" style="left:330px;top:150px;font-size:58px">100%</div>
  <div class="abs label-sm" style="left:332px;top:216px;width:180px">College Acceptance Rate</div>

  <svg class="abs" style="left:530px;top:144px" width="70" height="84" viewBox="0 0 70 84" aria-hidden="true">
    <path d="M24 4 H46 L40 18 H30 Z" fill="var(--orange)"/>
    <ellipse cx="35" cy="52" rx="30" ry="30" fill="var(--orange)"/>
    <text x="35" y="64" text-anchor="middle" font-family="Oswald,sans-serif" font-weight="700" font-size="34" fill="#fff">$</text>
  </svg>
  <div class="abs display num-blue" style="left:612px;top:146px;font-size:54px">$4.6M</div>
  <div class="abs label-sm" style="left:612px;top:208px;width:200px">in earned scholarships for 35 college students</div>

  <svg class="abs" style="left:850px;top:146px" width="60" height="90" viewBox="0 0 60 90" aria-hidden="true">
    <ellipse cx="30" cy="28" rx="22" ry="26" fill="none" stroke="var(--blue)" stroke-width="6"/>
    <rect x="27" y="54" width="6" height="34" rx="3" fill="var(--blue)"/>
    <circle cx="52" cy="70" r="6" fill="var(--orange)"/>
  </svg>
  <div class="abs display num-blue" style="left:922px;top:146px;font-size:66px">13</div>
  <div class="abs label" style="left:1000px;top:152px;width:180px;font-size:19px">National Urban Squash Titles</div>

  <!-- Row 2 -->
  <div class="abs photo" role="img" aria-label="Photo of academy students gathered outdoors beside a helicopter on a college visit"></div>
  <div class="abs label-sm" style="left:22px;top:512px;width:390px;font-size:17px">Accepted into some of the most illustrious colleges in the country</div>

  <svg class="abs" style="left:440px;top:284px" width="80" height="72" viewBox="0 0 80 72" aria-hidden="true">
    <path d="M40 70 L8 36 A18 18 0 0 1 40 12 A18 18 0 0 1 72 36 Z" fill="var(--orange)"/>
    <polyline points="14,38 30,38 36,26 44,50 50,38 66,38" fill="none" stroke="#fff" stroke-width="4"/>
  </svg>
  <div class="abs display num-blue" style="left:532px;top:280px;font-size:56px">100%</div>
  <div class="abs label-sm" style="left:532px;top:342px;width:250px">of students changed their eating habits in order to have a more healthy and balanced diet</div>
  <div class="abs display num-orange" style="left:440px;top:428px;font-size:54px">8.8%</div>
  <div class="abs label-sm" style="left:440px;top:488px;width:330px">positive swing in knowledge, understanding &amp; attitude to mental health issues</div>

  <!-- Student gender -->
  <div class="abs gender-head">Student Gender</div>
  <svg class="abs" style="left:820px;top:362px" width="110" height="190" viewBox="0 0 110 190" aria-hidden="true">
    <circle cx="55" cy="20" r="18" fill="var(--orange)"/>
    <path d="M55 42 L90 120 H20 Z" fill="var(--orange)"/>
    <rect x="36" y="120" width="14" height="62" fill="var(--orange)"/>
    <rect x="60" y="120" width="14" height="62" fill="var(--orange)"/>
  </svg>
  <div class="abs display num-orange" style="left:944px;top:380px;font-size:46px">72%</div>
  <div class="abs label-sm" style="left:946px;top:430px;font-weight:600;color:var(--orange)">Female</div>
  <svg class="abs" style="left:1080px;top:422px" width="80" height="130" viewBox="0 0 80 130" aria-hidden="true">
    <circle cx="40" cy="14" r="13" fill="var(--blue)"/>
    <rect x="18" y="30" width="44" height="52" rx="8" fill="var(--blue)"/>
    <rect x="22" y="80" width="14" height="46" fill="var(--blue)"/>
    <rect x="44" y="80" width="14" height="46" fill="var(--blue)"/>
  </svg>
  <div class="abs display num-blue" style="left:990px;top:478px;font-size:40px">28%</div>
  <div class="abs label-sm" style="left:1004px;top:522px;font-weight:600;color:var(--blue)">Male</div>

  <!-- Row 3 -->
  <svg class="abs" style="left:22px;top:598px" width="150" height="60" viewBox="0 0 150 60" aria-hidden="true">
    <polygon points="34,4 64,18 34,32 4,18" fill="var(--blue)"/><path d="M16 24 V38 Q34 48 52 38 V24 L34 34 Z" fill="var(--blue)"/>
    <polygon points="110,4 140,18 110,32 80,18" fill="var(--orange)"/><path d="M92 24 V38 Q110 48 128 38 V24 L110 34 Z" fill="var(--orange)"/>
  </svg>
  <div class="abs display num-blue" style="left:30px;top:664px;font-size:54px">2</div>
  <div class="abs label-sm" style="left:72px;top:672px;width:200px">Horizon Millennium Scholars</div>

  <svg class="abs" style="left:320px;top:600px" width="150" height="62" viewBox="0 0 150 62" aria-hidden="true">
    <g font-family="Open Sans,sans-serif" font-size="11" font-weight="700" fill="var(--blue)">
      <rect x="0" y="0" width="44" height="18" fill="none" stroke="var(--blue)" stroke-width="2"/><text x="22" y="13" text-anchor="middle">2010</text>
      <rect x="52" y="0" width="44" height="18" fill="none" stroke="var(--blue)" stroke-width="2"/><text x="74" y="13" text-anchor="middle">2011</text>
      <rect x="104" y="0" width="44" height="18" fill="none" stroke="var(--blue)" stroke-width="2"/><text x="126" y="13" text-anchor="middle">2012</text>
      <rect x="26" y="28" width="44" height="18" fill="none" stroke="var(--orange)" stroke-width="2"/><text x="48" y="41" text-anchor="middle" fill="var(--orange)">2013</text>
      <rect x="78" y="28" width="44" height="18" fill="none" stroke="var(--orange)" stroke-width="2"/><text x="100" y="41" text-anchor="middle" fill="var(--orange)">2014</text>
    </g>
  </svg>
  <div class="abs label-sm" style="left:490px;top:596px">Over</div>
  <div class="abs display num-blue" style="left:488px;top:618px;font-size:48px">4600</div>
  <div class="abs label-sm" style="left:490px;top:672px;width:150px">hours of programming</div>

  <div class="abs display num-blue" style="left:660px;top:606px;font-size:50px">GPA <span class="num-orange">3.7</span></div>
  <div class="abs label-sm" style="left:662px;top:664px">Class average</div>

  <svg class="abs" style="left:880px;top:596px" width="96" height="96" viewBox="0 0 42 42" aria-hidden="true">
    <circle cx="21" cy="21" r="15.915" fill="none" stroke="var(--rule)" stroke-width="10"/>
    <circle cx="21" cy="21" r="15.915" fill="none" stroke="var(--orange)" stroke-width="10" stroke-dasharray="91 9" stroke-dashoffset="25"/>
  </svg>
  <div class="abs display num-blue" style="left:990px;top:604px;font-size:56px">91%</div>
  <div class="abs label-sm" style="left:992px;top:664px;width:170px">student retention rate</div>

  <!-- Row 4: ethnicity + finance -->
  <div class="abs eth-box"></div>
  <div class="abs eth-title">Ethnicity</div>
  <svg class="abs" style="left:170px;top:792px" width="190" height="190" viewBox="0 0 42 42" role="img" aria-label="Ethnicity donut chart">
    <circle cx="21" cy="21" r="15.915" fill="none" stroke="var(--orange)" stroke-width="7" stroke-dasharray="62 38" stroke-dashoffset="25"/>
    <circle cx="21" cy="21" r="15.915" fill="none" stroke="var(--blue)" stroke-width="7" stroke-dasharray="28 72" stroke-dashoffset="63"/>
    <circle cx="21" cy="21" r="15.915" fill="none" stroke="var(--blue-dark)" stroke-width="7" stroke-dasharray="6 94" stroke-dashoffset="35"/>
    <circle cx="21" cy="21" r="15.915" fill="none" stroke="var(--grey)" stroke-width="7" stroke-dasharray="4 96" stroke-dashoffset="29"/>
    <g font-family="Open Sans,sans-serif" font-size="3.2" font-weight="700" fill="#fff" text-anchor="middle">
      <text x="35" y="28">62%</text><text x="8" y="18">28%</text><text x="15" y="6.5">6%</text>
    </g>
  </svg>
  <div class="abs" style="left:40px;top:986px;display:grid;grid-template-columns:200px 200px;gap:6px 10px">
    <span class="legend"><i class="swatch" style="background:var(--orange)"></i>Hispanics</span>
    <span class="legend"><i class="swatch" style="background:var(--blue)"></i>Asian/Pacific Islander</span>
    <span class="legend"><i class="swatch" style="background:var(--blue-dark)"></i>African American</span>
    <span class="legend"><i class="swatch" style="background:var(--grey)"></i>Caucasian</span>
  </div>

  <div class="abs" style="left:500px;top:722px;display:flex;flex-direction:column;gap:4px">
    <span class="legend"><i class="swatch" style="background:var(--orange)"></i>Total Revenue*</span>
    <span class="legend"><i class="swatch" style="background:var(--blue)"></i>Expenses</span>
    <span class="label-sm" style="font-size:12px;color:var(--grey)">*As per 990 returns</span>
  </div>
  <svg class="abs" style="left:490px;top:700px" width="690" height="350" viewBox="0 0 690 350" role="img" aria-label="Revenue and expenses 2010 to 2014">
    <line x1="10" y1="310" x2="680" y2="310" stroke="var(--rule)" stroke-width="2"/>
    <g font-family="Open Sans,sans-serif" font-size="14" font-weight="700">
      <rect x="40" y="257" width="40" height="53" fill="var(--orange)"/><rect x="84" y="258" width="40" height="52" fill="var(--blue)"/>
      <text transform="translate(66 250) rotate(-90)" fill="var(--orange)">$241,783</text>
      <text transform="translate(110 250) rotate(-90)" fill="var(--blue)">$235,853</text>
      <rect x="170" y="240" width="40" height="70" fill="var(--orange)"/><rect x="214" y="242" width="40" height="68" fill="var(--blue)"/>
      <text transform="translate(196 233) rotate(-90)" fill="var(--orange)">$315,269</text>
      <text transform="translate(240 233) rotate(-90)" fill="var(--blue)">$307,210</text>
      <rect x="300" y="234" width="40" height="76" fill="var(--orange)"/><rect x="344" y="237" width="40" height="73" fill="var(--blue)"/>
      <text transform="translate(326 227) rotate(-90)" fill="var(--orange)">$344,398</text>
      <text transform="translate(370 227) rotate(-90)" fill="var(--blue)">$329,418</text>
      <rect x="430" y="61" width="40" height="249" fill="var(--orange)"/><rect x="474" y="63" width="40" height="247" fill="var(--blue)"/>
      <text transform="translate(456 170) rotate(-90)" fill="#fff">$1,126,377</text>
      <text transform="translate(500 170) rotate(-90)" fill="#fff">$1,116,587</text>
      <rect x="560" y="184" width="40" height="126" fill="var(--orange)"/><rect x="604" y="186" width="40" height="124" fill="var(--blue)"/>
      <text transform="translate(586 268) rotate(-90)" fill="#fff">$568,745</text>
      <text transform="translate(630 268) rotate(-90)" fill="#fff">$559,176</text>
      <g font-size="18" fill="var(--blue)" text-anchor="middle">
        <text x="82" y="336">2010</text><text x="212" y="336">2011</text><text x="342" y="336">2012</text><text x="472" y="336">2013</text><text x="602" y="336">2014</text>
      </g>
    </g>
  </svg>

  <!-- Left column: community -->
  <div class="abs badge" role="img" aria-label="Gold level nonprofit listing badge"></div>
  <div class="abs label-sm" style="left:30px;top:1244px;width:370px;font-size:17px">Pathway Youth Academy is a Gold level CharityLens Nonprofit</div>
  <div class="abs rule" style="left:30px;top:1310px;width:370px"></div>
  <div class="abs display num-blue" style="left:30px;top:1334px;font-size:84px">687</div>
  <div class="abs label-sm" style="left:190px;top:1340px;width:210px;font-size:16px">student volunteer hours donated to <b>29</b> community projects across San Diego County</div>
  <div class="abs rule" style="left:30px;top:1450px;width:370px"></div>
  <div class="abs display num-orange" style="left:30px;top:1474px;font-size:84px">385</div>
  <div class="abs label-sm" style="left:30px;top:1568px;width:370px;font-size:16px">of volunteer service in squash and academic worth <b>$834.48</b> in professional support</div>
  <div class="abs rule" style="left:30px;top:1640px;width:370px"></div>
  <div class="abs display num-blue" style="left:30px;top:1664px;font-size:84px">87%</div>
  <svg class="abs" style="left:220px;top:1670px" width="170" height="60" viewBox="0 0 170 60" aria-hidden="true">
    <g fill="none" stroke="var(--blue)" stroke-width="2"><rect x="2" y="2" width="50" height="22"/><rect x="60" y="2" width="50" height="22"/><rect x="118" y="2" width="50" height="22"/><rect x="30" y="34" width="50" height="22" stroke="var(--orange)"/><rect x="88" y="34" width="50" height="22" stroke="var(--orange)"/></g>
  </svg>
  <div class="abs label-sm" style="left:30px;top:1758px;width:370px;font-size:16px">attendance rate at an average of <b>99</b> days of programming per student</div>

  <!-- 2016 panel -->
  <div class="abs progress"></div>
  <div class="abs progress-year">2016</div>
  <div class="abs progress-tag">A YEAR OF<br>CONTINUED PROGRESS</div>
  <svg class="abs" style="left:450px;top:1224px" width="66" height="80" viewBox="0 0 70 84" aria-hidden="true">
    <path d="M24 4 H46 L40 18 H30 Z" fill="var(--orange)"/>
    <ellipse cx="35" cy="52" rx="30" ry="30" fill="var(--orange)"/>
    <text x="35" y="64" text-anchor="middle" font-family="Oswald,sans-serif" font-weight="700" font-size="34" fill="#fff">$</text>
  </svg>
  <div class="abs income-figure">$564,729</div>
  <div class="abs income-label">Income</div>
  <svg class="abs" style="left:450px;top:1360px" width="420" height="420" viewBox="0 0 42 42" role="img" aria-label="2016 income sources donut chart">
    <circle cx="21" cy="21" r="15.915" fill="none" stroke="#f78f20" stroke-width="8" stroke-dasharray="48 52" stroke-dashoffset="25"/>
    <circle cx="21" cy="21" r="15.915" fill="none" stroke="#fab066" stroke-width="8" stroke-dasharray="20 80" stroke-dashoffset="77"/>
    <circle cx="21" cy="21" r="15.915" fill="none" stroke="#fcd2a4" stroke-width="8" stroke-dasharray="15 85" stroke-dashoffset="57"/>
    <circle cx="21" cy="21" r="15.915" fill="none" stroke="#b86612" stroke-width="8" stroke-dasharray="13 87" stroke-dashoffset="42"/>
    <circle cx="21" cy="21" r="15.915" fill="none" stroke="#8a4a08" stroke-width="8" stroke-dasharray="4 96" stroke-dashoffset="29"/>
    <g font-family="Open Sans,sans-serif" font-size="2.4" font-weight="700" fill="#fff" text-anchor="middle">
      <text x="36.5" y="25">48%</text><text x="17" y="37.5">20%</text><text x="6" y="22">15%</text><text x="11" y="9">13%</text><text x="19" y="5.6">4%</text>
    </g>
  </svg>
  <div class="abs income-legend">
    <span class="legend"><i class="swatch" style="background:#f78f20"></i>Foundations - $273,650</span>
    <span class="legend"><i class="swatch" style="background:#fab066"></i>Individuals - $114,821</span>
    <span class="legend"><i class="swatch" style="background:#fcd2a4"></i>Board - $82,580</span>
    <span class="legend"><i class="swatch" style="background:#b86612"></i>Events - $71,546</span>
    <span class="legend"><i class="swatch" style="background:#8a4a08"></i>Corporations - $22,132</span>
  </div>

  <!-- Bottom -->
  <div class="abs display num-blue" style="left:430px;top:1950px;font-size:80px">77.5%</div>
  <div class="abs label-sm" style="left:432px;top:2046px;width:310px;font-size:17px">participation in summer programs, scholarships and internships</div>
  <div class="abs partners">
    <div class="partner"><span class="partner-mark"></span>Wide World Society</div>
    <div class="partner"><span class="partner-mark"></span>Brightwell Children's</div>
    <div class="partner"><span class="partner-mark"></span>Harbor Trust &amp; Co.</div>
    <div class="partner"><span class="partner-mark"></span>Teach Forward Corps</div>
    <div class="partner"><span class="partner-mark"></span>Northstar Media</div>
  </div>
</div>
</body>
</html>
```